Halvard Atelier Business cards

Design our business cards and eventually a logo. The company is based in Paris, its activity is the retailing via internet of luxury home furniture (like Vambrelli, Bercusa, tarvoni...) Our clients are international andwith a high sense of aesthetics. The design shall communicate wealth and trust with a high quality and aesthetic sense, pure lines Company Name is Halvard AtelierExplanation of the name: usually people who wants to buy furniture usually go in a showroom. Today they go in showroom to test the furniture and they search for the price on internet, which is a "Halvard atelier".We will not be a e-commerce site. Our site will be (another project) a presentation site which purpose is to reach qualified prospects. Then everything will be handled by phone, meeting etc.The business card must be professional as we will negotiate with many luxury brands, opportunity to represent them on our site, prices etc.As far as the color are concerned mostly black and whithe or grey. The font of the Halvard Atelier name shall have some impact.

Target Market(s)

High-end furniture and buyers of luxury goods, international customers, mostly women who handle such projects.
We also deal with professional buyers (hotels as an example) and luxury brands

Contact Information for Business Card

standard format 85x55, lanscape card, square corners will be printed on thick high quality paper (300 or 350g)

Font styles to use
Sans Serif

Colors

Designer to choose colors to be used in the design.

Requirements
Must have
• Must be white, as the paper will be high quality, the paper will enhance the card.
• Name of the brand Halvard atelier (with specific font which make it very nice looking and catch the attention. similar to Calibri or Calibri
• Name of person (will give you the name later (4 names and position)
• the position of the person
• Mobile phone, e-mail, Physical address 27, rue Fenouillard, 75005 Paris, France (courrier only) our web site www.halvardatelier.fr
• The card must be simple and class
Nice to have
• Font of the address is smaller than the rest,
• Calibri font or similar on recto side with the name of the company which may look similar to the picture inserted in the brief.
• The grey color in the picture inserted is ok for us
Should not have
• Any parallel lines which represent the name of the company
• Any heavy design If you go on internet sites which present the furniture all designs are pure lines and high quality craftsmanship. To have an idea of our targetted client or brand we will be in touch: https://www.casavelumi.it/projects/
• Note that the picture added below is what we use, now as mail signature, up to you to have a better design etc.

```html
<!DOCTYPE html>
<html lang="en">
<head>
<meta charset="utf-8">
<title>Halvard Atelier — Business Cards</title>
<link rel="stylesheet" href="https://fonts.googleapis.com/css2?family=Josefin+Sans:wght@600&family=Ubuntu:wght@400&family=Crimson+Text:ital@1&display=swap">
<style>
  :root {
    --backdrop: #3b3531;
    --paper: #f1f1ef;
    --ink: #5e5e5e;
    --ink-soft: #7a7a7a;
    --shadow: rgba(0, 0, 0, 0.35);
  }
  * { margin: 0; padding: 0; box-sizing: border-box; }
  html, body {
    width: 1200px;
    height: 672px;
    overflow: hidden;
    background: var(--backdrop);
  }
  .stage {
    position: relative;
    width: 1200px;
    height: 672px;
  }
  .card {
    position: absolute;
    top: 174px;
    width: 500px;
    height: 324px;
    background: var(--paper);
    box-shadow: 0 6px 18px var(--shadow);
    color: var(--ink);
  }
  .card--front { left: 70px; }
  .card--back { left: 630px; }

  /* Front */
  .person {
    position: absolute;
    left: 64px;
    top: 150px;
  }
  .person__name {
    font-family: "Josefin Sans", sans-serif;
    font-weight: 600;
    font-size: 19px;
    letter-spacing: 1.5px;
    text-transform: uppercase;
    color: var(--ink);
  }
  .person__role {
    margin-top: 2px;
    font-family: "Crimson Text", serif;
    font-style: italic;
    font-size: 13px;
    color: var(--ink-soft);
  }
  .contacts {
    position: absolute;
    left: 290px;
    top: 56px;
    list-style: none;
    font-family: "Ubuntu", sans-serif;
    font-size: 12px;
    line-height: 1.55;
    color: var(--ink);
  }
  .contacts li {
    display: flex;
    align-items: center;
    gap: 7px;
  }
  .contacts svg {
    width: 10px;
    height: 10px;
    flex: none;
    fill: var(--ink);
  }
  .contacts .address-line { padding-left: 17px; font-size: 11px; }
  .contacts .address { font-size: 11px; }

  /* Back */
  .brand {
    position: absolute;
    inset: 0;
    display: flex;
    flex-direction: column;
    align-items: center;
    justify-content: center;
    gap: 16px;
  }
  .brand__square {
    width: 22px;
    height: 22px;
    background: var(--ink);
  }
  .brand__name {
    font-family: "Josefin Sans", sans-serif;
    font-weight: 600;
    font-size: 27px;
    letter-spacing: 2.5px;
    text-transform: uppercase;
    color: var(--ink);
  }
</style>
</head>
<body>
<main class="stage">
  <section class="card card--front" aria-label="Business card front">
    <div class="person">
      <p class="person__name">Corentin Malavert</p>
      <p class="person__role">Président and Co-Founder</p>
    </div>
    <ul class="contacts">
      <li>
        <svg viewBox="0 0 10 10" aria-hidden="true"><path d="M2 0.5h2l1 2.5-1.3 1a6 6 0 0 0 2.3 2.3l1-1.3 2.5 1v2A1 1 0 0 1 8.5 9.5 8 8 0 0 1 0.5 1.5 1 1 0 0 1 2 0.5z"/></svg>
        <span>+33 6 41 27 93 08</span>
      </li>
      <li>
        <svg viewBox="0 0 10 10" aria-hidden="true"><path d="M0.5 2h9v6h-9z M1 2.5l4 3 4-3" fill="none" stroke="currentColor" stroke-width="1" style="stroke:#5e5e5e"/></svg>
        <span>corentin@halvardatelier.fr</span>
      </li>
      <li>
        <svg viewBox="0 0 10 10" aria-hidden="true"><g fill="none" stroke="#5e5e5e" stroke-width="0.9"><circle cx="5" cy="5" r="4.3"/><ellipse cx="5" cy="5" rx="1.8" ry="4.3"/><path d="M0.7 5h8.6M1.5 2.8h7M1.5 7.2h7"/></g></svg>
        <span>www.halvardatelier.fr</span>
      </li>
      <li class="address">
        <svg viewBox="0 0 10 10" aria-hidden="true"><path d="M5 0.3a3.4 3.4 0 0 0-3.4 3.4C1.6 6.2 5 9.7 5 9.7s3.4-3.5 3.4-6A3.4 3.4 0 0 0 5 0.3zm0 4.7a1.3 1.3 0 1 1 0-2.6 1.3 1.3 0 0 1 0 2.6z"/></svg>
        <span>27 rue Fenouillard</span>
      </li>
      <li class="address-line">75005 Paris, France</li>
    </ul>
  </section>

  <section class="card card--back" aria-label="Business card back">
    <div class="brand">
      <span class="brand__square" aria-hidden="true"></span>
      <p class="brand__name">Halvard Atelier</p>
    </div>
  </section>
</main>
</body>
</html>
```